Heronfield Global Trade & Heritage Link Landing Page Design

We are a Chinese high-end bespoke business travel company. We want to design a landing page, to promote our brand and business, to attract target clients for business development.

We have own logo, like design in modern simple style, like to sample as attached. Like the Sample 2, use different color to display our business services.

We want to mainly display 7 parts of business:
1. Visa Services
2. International Hotel Reservation
3. Worldwide Flight Tickets Booking
4. Worldwide Travel Arrangement
5. VIP Airport Concierge
6. Duty Free Goods
7. International Business Resources

We imagine design a world map, points out popular countries, cities, and destinations, and combine with our own business resources cities.

Design in modern, business, international style. Thank you. Look forward to cooperate with you.

Target Market(s)

Business Clients and High income private client

Industry/Entity Type

Tourism, Business Travel, International Exchange

Coding

Coded - Design and coding required

Requirements
Must have
• Our logo, large images, design a world map

```html
<!DOCTYPE html>
<html lang="en">
<head>
<meta charset="utf-8">
<title>Heronfield Global — Bespoke Business Travel</title>
<link href="https://fonts.googleapis.com/css2?family=Jost:wght@400;500;600;700&family=Open+Sans:wght@400;600;700&display=swap" rel="stylesheet">
<style>
:root{
  --orange:#f5a63a;
  --green:#7cc36f;
  --teal:#1fb1c6;
  --grad:linear-gradient(90deg,var(--orange),var(--green) 55%,var(--teal));
  --navy:#1b2a3a;
  --ink:#2b2f36;
  --muted:#5c6470;
  --deep-teal:#0e5a6c;
  --ice:#eaf7fb;
  --map-tone:#b9bfc6;
  --map-soft:#e4e7ea;
  --white:#fff;
}
*{box-sizing:border-box;margin:0;padding:0}
html,body{width:1200px;height:4166px;overflow:hidden}
body{font-family:"Open Sans",sans-serif;color:var(--ink);background:var(--white);position:relative}
.abs{position:absolute}
.heading{font-family:"Jost",sans-serif;font-weight:600;letter-spacing:2.5px;color:var(--navy)}
.eyebrow{font-family:"Jost",sans-serif;font-size:14px;font-weight:600;letter-spacing:5px;
  background:var(--grad);-webkit-background-clip:text;background-clip:text;color:transparent}
.center.eyebrow{width:auto;left:50%;transform:translateX(-50%)}
.pill{border-radius:30px;background:var(--grad);color:#fff;font-weight:600;text-align:center}
.arrow-dot{width:24px;height:24px;flex:none;border-radius:50%;background:var(--grad);display:flex;align-items:center;justify-content:center}

/* hero */
.hero{left:0;top:0;width:1200px;height:660px;overflow:hidden}
.hero-photo{left:0;top:0;width:1200px;height:600px;
  background:linear-gradient(100deg,#1c3f98 0%,#2d5fb9 30%,#6e86c4 55%,#b9a9b6 72%,#4a6b8f 85%,#27405f 100%)}
.brand{left:137px;top:34px;display:flex;align-items:center;gap:10px}
.brand-mark{width:40px;height:40px;border-radius:50%;background:var(--white)}
.brand-name{font-family:"Jost",sans-serif;font-weight:700;font-size:22px;letter-spacing:1.5px;color:var(--white);line-height:1}
.nav{left:603px;top:49px;display:flex;gap:24px;font-size:12.5px;color:#2a3550;font-weight:600}
.nav-cta{left:901px;top:36px;width:120px;height:42px;line-height:42px;font-size:12.5px}
.welcome{left:132px;top:203px;color:#fff;font-family:"Jost",sans-serif;font-size:21px;letter-spacing:2.5px;font-weight:500}
.hero-title{left:130px;top:245px;color:#fff;font-family:"Jost",sans-serif;font-weight:700;font-size:52px;line-height:60px;letter-spacing:4px}
.tagline{left:130px;top:388px;color:#fff;font-size:15px;font-weight:700}

.booking{left:663px;top:162px;width:362px;height:452px;background:#fff;box-shadow:0 10px 40px rgba(20,40,80,.18)}
.booking h2{position:absolute;left:32px;top:36px;font-family:"Jost",sans-serif;font-size:19px;font-weight:600;letter-spacing:2px;color:var(--navy)}
.booking p{position:absolute;left:32px;top:66px;width:300px;font-size:10.5px;line-height:16px;color:var(--muted)}
.booking .rule{position:absolute;left:32px;top:112px;width:80px;height:3px;background:var(--grad)}
.field{position:absolute;left:32px;width:297px;height:52px;border:1px solid #d9dde3;border-radius:4px;display:flex;align-items:center;font-size:12px;color:#4a5260}
.field .ico{width:42px;height:100%;border-right:1px solid #d9dde3;display:flex;align-items:center;justify-content:center;margin-right:12px}
.book-btn{position:absolute;left:32px;top:358px;width:297px;height:56px;line-height:56px;font-size:13px;box-shadow:0 6px 14px rgba(60,170,150,.35)}

/* about */
.about-photo{left:560px;top:790px;width:640px;height:490px;
  background:radial-gradient(ellipse at 75% 55%,#d9c2ad 0%,#e9ddd1 25%,#f4f1ee 50%,rgba(255,255,255,0) 75%)}
.about-ring{left:130px;top:752px;width:405px;height:405px;border-radius:50%;
  background:conic-gradient(from 200deg,var(--orange),var(--green),var(--teal),var(--orange))}
.about-img{left:148px;top:770px;width:369px;height:369px;border-radius:50%;border:6px solid #fff;
  background:linear-gradient(150deg,#eef0f2,#b9c2c8 45%,#7d6e5c 80%,#5a4b3f)}
.about-text{left:605px;top:815px;width:380px}
.about-text h2{font-size:32px;line-height:38px;margin:14px 0 32px}
.about-text p{font-size:12.5px;line-height:21px;color:var(--muted);margin-bottom:14px}

/* services */
.services{left:0;top:1285px;width:1200px;height:945px;background:linear-gradient(180deg,var(--ice),#f3fbfd 60%,var(--ice))}
.center{left:0;width:1200px;text-align:center}
.sec-title{font-size:31px}
.sec-sub{font-size:12.5px;line-height:21px;color:var(--ink)}
.card{width:234px;height:284px;background:#fff;box-shadow:0 4px 14px rgba(0,0,0,.06)}
.card .img{height:230px}
.card .label{height:54px;display:flex;align-items:center;justify-content:space-between;padding:0 16px;font-size:11.5px;line-height:17px;font-weight:600;color:var(--navy)}
.contact-btn{left:540px;top:2143px;width:120px;height:44px;line-height:44px;font-size:12.5px}

/* explore */
.search{left:414px;top:2466px;width:368px;height:38px;background:#fff;box-shadow:0 3px 12px rgba(0,0,0,.1);display:flex;align-items:center;font-size:12px;color:#444}
.search .go{margin-left:auto;width:66px;height:38px;background:linear-gradient(90deg,var(--orange),var(--green));display:flex;align-items:center;justify-content:center}
.map{left:150px;top:2552px;width:840px;height:356px;border-radius:28px;
  background:
    radial-gradient(ellipse 30% 45% at 22% 40%,var(--map-tone),rgba(185,191,198,0) 100%),
    radial-gradient(ellipse 32% 50% at 58% 45%,var(--map-tone),rgba(185,191,198,0) 100%),
    radial-gradient(ellipse 14% 24% at 88% 80%,var(--map-tone),rgba(185,191,198,0) 100%),
    linear-gradient(180deg,var(--map-soft),#f2f4f6);
  border:1px solid #dde1e5}
.city-card{left:555px;top:2536px;width:190px;height:76px;background:#fff;box-shadow:0 4px 14px rgba(0,0,0,.12);display:flex;gap:10px;padding:6px;z-index:2}
.city-card .thumb{width:54px;height:64px;flex:none;background:linear-gradient(180deg,#7a8fb3,#3d4f78)}
.city-card b{font-size:11px}
.city-card span{display:block;font-size:9px;color:var(--muted);line-height:12px;margin:2px 0}
.city-card em{font-style:normal;font-size:8.5px;color:var(--orange)}
.pin{z-index:2}

/* blog */
.blog-card{top:3145px;width:280px;height:375px;color:#fff;text-align:center;overflow:hidden}
.blog-card .date{display:inline-block;background:#fff;color:var(--ink);border-radius:20px;padding:6px 22px;font-size:12px}
.blog-card h3{font-family:"Jost",sans-serif;font-size:21px;font-weight:600;line-height:28px;margin:12px 20px}
.blog-card p{font-size:13px;line-height:24px;margin:0 14px 14px;opacity:.95}
.blog-card .more{font-family:"Jost",sans-serif;font-size:16px;font-weight:600;letter-spacing:.5px}
.nav-arrow{top:3313px;width:48px;height:48px;border-radius:50%;background:#8a8f96;border:2px solid #fff;display:flex;align-items:center;justify-content:center}

/* footer */
.footer-photo{left:0;top:3520px;width:1200px;height:330px;background:linear-gradient(180deg,#fff 0%,#c9d6dd 25%,#8fa4ad 60%,#5d7a86 100%)}
.footer{left:0;top:3700px;width:1200px;height:466px}
.f-brand{left:105px;top:3889px;display:flex;align-items:center;gap:10px}
.f-about{left:105px;top:3958px;width:280px;font-size:10.5px;line-height:18px;color:#cfe2e8}
.f-follow{left:105px;top:4057px;font-size:11px;color:#fff;display:flex;align-items:center;gap:10px}
.f-follow i{width:10px;height:10px;border-radius:50%;background:#fff;display:inline-block}
.f-col{top:3866px;color:#dce9ee;font-size:11px}
.f-col h4{font-family:"Jost",sans-serif;color:#fff;font-size:13px;font-weight:600;letter-spacing:1px;margin-bottom:18px}
.f-col li{list-style:none;line-height:26px}
.f-contact li{display:flex;gap:8px;line-height:20px;margin-bottom:14px;font-size:12px}
.f-rule{left:105px;top:4116px;width:1008px;height:1px;background:rgba(255,255,255,.3)}
.copy{left:0;top:4133px;width:1200px;text-align:center;font-size:10.5px;color:#dce9ee}
</style>
</head>
<body>

<!-- HERO -->
<section class="abs hero">
  <div class="abs hero-photo" role="img" aria-label="Photo of a luxury waterfront resort at dusk with loungers and sea"></div>
  <svg class="abs" style="left:0;top:0" width="1200" height="660" viewBox="0 0 1200 660">
    <path d="M0 420 C120 560 330 600 560 590 C760 580 1000 540 1200 560 L1200 660 L0 660Z" fill="#fff"/>
    <path d="M0 420 C90 520 260 560 460 555 C330 560 150 530 0 450Z" fill="#0b8fb8"/>
    <path d="M75 460 C180 520 320 545 440 542 C300 540 160 505 75 460Z" fill="#f2c23e"/>
    <path d="M350 640 C520 630 620 605 700 580 L700 600 C620 625 500 640 350 640Z" fill="#f2b632"/>
    <path d="M1000 540 C1080 540 1150 548 1200 556 L1200 545 C1150 538 1080 536 1000 540Z" fill="#1fb1c6"/>
  </svg>
  <div class="abs brand"><span class="brand-mark"></span><span class="brand-name">HERONFIELD<br>GLOBAL</span></div>
  <nav class="abs nav"><span>ABOUT US</span><span>SERVICES</span><span>NEWS AND BLOG</span></nav>
  <div class="abs pill nav-cta">CONTACT US</div>
  <div class="abs welcome">WELCOME TO</div>
  <h1 class="abs hero-title">HERONFIELD<br>GLOBAL</h1>
  <div class="abs tagline">High-End Bespoke Business Travel Company</div>

  <form class="abs booking">
    <h2>BOOK AN APPOINTMENT</h2>
    <p>Plan your next business trip effortlessly and efficiently by booking an appointment with our expert travel advisors.</p>
    <span class="rule"></span>
    <div class="field" style="top:136px"><span class="ico"><svg width="14" height="14" viewBox="0 0 14 14" fill="none" stroke="#555" stroke-width="1.2"><circle cx="7" cy="4.5" r="2.8"/><path d="M1.5 13c.5-3 2.8-4.5 5.5-4.5S12 10 12.5 13"/></svg></span>Enter &nbsp;Your Name</div>
    <div class="field" style="top:202px"><span class="ico"><svg width="14" height="12" viewBox="0 0 14 12" fill="none" stroke="#555" stroke-width="1.2"><rect x="1" y="1.5" width="12" height="9"/><path d="M1 2l6 5 6-5"/></svg></span>Enter &nbsp;Your Email</div>
    <div class="field" style="top:274px"><span class="ico"><svg width="12" height="15" viewBox="0 0 12 15" fill="none" stroke="#555" stroke-width="1.2"><path d="M6 14s5-5 5-8.5A5 5 0 0 0 1 5.5C1 9 6 14 6 14z"/><circle cx="6" cy="5.5" r="1.8"/></svg></span>Search Destination</div>
    <div class="pill book-btn">BOOK NOW</div>
  </form>
</section>

<!-- ABOUT -->
<section>
  <div class="abs about-photo" role="img" aria-label="Faded photo of a businesswoman holding a coffee cup by the sea"></div>
  <div class="abs about-ring"></div>
  <div class="abs about-img" role="img" aria-label="Photo of a bright hotel restaurant with tables and large windows"></div>
  <div class="abs about-text">
    <div class="eyebrow">ABOUT</div>
    <h2 class="heading">Elevate Your Business<br>Travel Experience</h2>
    <p>At our high-end bespoke business travel company, we understand that business travel is more than just a trip.</p>
    <p>It's an opportunity to expand your horizons, forge new connections, and make lasting impressions. That's why we offer a range of tailored services to help you achieve your goals, wherever your travels take you.</p>
  </div>
</section>

<!-- SERVICES -->
<section class="abs services"></section>
<div class="abs center eyebrow" style="top:1343px">SERVICES</div>
<h2 class="abs center heading sec-title" style="top:1367px">We Provide Exclusive Services</h2>
<p class="abs center sec-sub" style="top:1417px">We aim to showcase the 7 key parts of our business that set us apart<br>from the rest.</p>

<div class="abs card" style="left:100px;top:1501px"><div class="img" role="img" aria-label="Photo of a smiling agent handing over a passport" style="background:linear-gradient(160deg,#c9c3bd,#8a6b5a 60%,#e7e2dc)"></div><div class="label"><span>VISA SERVICES</span><span class="arrow-dot"><svg width="12" height="10" viewBox="0 0 12 10" fill="none" stroke="#fff" stroke-width="1.8"><path d="M1 5h9M6 1l4 4-4 4"/></svg></span></div></div>
<div class="abs card" style="left:358px;top:1501px"><div class="img" role="img" aria-label="Photo of a receptionist on the phone at a hotel desk" style="background:linear-gradient(160deg,#9e8e7e,#6d4a3a 55%,#d7d1ca)"></div><div class="label"><span>INTERNATIONAL HOTEL<br>RESERVATION</span><span class="arrow-dot"><svg width="12" height="10" viewBox="0 0 12 10" fill="none" stroke="#fff" stroke-width="1.8"><path d="M1 5h9M6 1l4 4-4 4"/></svg></span></div></div>
<div class="abs card" style="left:617px;top:1501px"><div class="img" role="img" aria-label="Photo of flight tickets and a passport on a travel bag" style="background:linear-gradient(160deg,#6b6f74,#b9bec4 50%,#3a3d42)"></div><div class="label"><span>WORLDWIDE FLIGHT<br>TICKETS BOOKING</span><span class="arrow-dot"><svg width="12" height="10" viewBox="0 0 12 10" fill="none" stroke="#fff" stroke-width="1.8"><path d="M1 5h9M6 1l4 4-4 4"/></svg></span></div></div>
<div class="abs card" style="left:875px;top:1501px"><div class="img" role="img" aria-label="Photo of hands on a travel map beside a coffee cup" style="background:linear-gradient(160deg,#d9c9a8,#9fc0c9 50%,#c7a77a)"></div><div class="label"><span>WORLDWIDE TRAVEL<br>ARRANGEMENT</span><span class="arrow-dot"><svg width="12" height="10" viewBox="0 0 12 10" fill="none" stroke="#fff" stroke-width="1.8"><path d="M1 5h9M6 1l4 4-4 4"/></svg></span></div></div>
<div class="abs card" style="left:229px;top:1818px"><div class="img" role="img" aria-label="Photo of a businessman in a suit at an airport" style="background:linear-gradient(160deg,#d6dde2,#2b3f73 55%,#b7c0c8)"></div><div class="label"><span>VIP AIRPORT CONCIERGE</span><span class="arrow-dot"><svg width="12" height="10" viewBox="0 0 12 10" fill="none" stroke="#fff" stroke-width="1.8"><path d="M1 5h9M6 1l4 4-4 4"/></svg></span></div></div>
<div class="abs card" style="left:487px;top:1818px"><div class="img" role="img" aria-label="Photo of a duty free shop interior" style="background:linear-gradient(180deg,#b47a3a,#d9a764 30%,#e6e0d8 60%,#c46b7a)"></div><div class="label"><span>DUTY FREE GOODS</span><span class="arrow-dot"><svg width="12" height="10" viewBox="0 0 12 10" fill="none" stroke="#fff" stroke-width="1.8"><path d="M1 5h9M6 1l4 4-4 4"/></svg></span></div></div>
<div class="abs card" style="left:745px;top:1818px"><div class="img" role="img" aria-label="Photo of hands typing on a laptop with a teal overlay" style="background:linear-gradient(160deg,#a7c9c9,#3f7f84 55%,#1e4f55)"></div><div class="label"><span>INTERNATIONAL<br>BUSINESS RESOURCES</span><span class="arrow-dot"><svg width="12" height="10" viewBox="0 0 12 10" fill="none" stroke="#fff" stroke-width="1.8"><path d="M1 5h9M6 1l4 4-4 4"/></svg></span></div></div>
<div class="abs pill contact-btn">CONTACT US</div>

<!-- EXPLORE -->
<div class="abs center eyebrow" style="top:2312px">EXPLORE</div>
<h2 class="abs center heading sec-title" style="top:2337px">Popular Destinations</h2>
<p class="abs center sec-sub" style="top:2390px">Explore top spots worldwide, connect with locals, and upgrade your trips in Shanghai, New York,<br>and more with our insider expertise.</p>
<div class="abs search">
  <svg style="margin:0 10px 0 16px" width="12" height="15" viewBox="0 0 12 15" fill="none" stroke="#555" stroke-width="1.2"><path d="M6 14s5-5 5-8.5A5 5 0 0 0 1 5.5C1 9 6 14 6 14z"/><circle cx="6" cy="5.5" r="1.8"/></svg>
  Search Destination
  <span class="go"><svg width="18" height="18" viewBox="0 0 18 18" fill="none" stroke="#fff" stroke-width="1.8"><circle cx="7.5" cy="7.5" r="5.5"/><path d="M11.5 11.5l5 5"/></svg></span>
</div>
<div class="abs map" role="img" aria-label="Dotted grey world map of all continents with featured destinations London and Sydney marked"></div>
<div class="abs city-card"><div class="thumb" role="img" aria-label="Photo of a London bridge at dusk"></div><div><b>London</b><span>Lorem ipsum dolor sit amet consectetur.</span><em>READ MORE</em></div></div>
<svg class="abs pin" style="left:546px;top:2628px" width="52" height="68" viewBox="0 0 52 68"><path d="M26 66C26 66 50 40 50 24A24 24 0 0 0 2 24C2 40 26 66 26 66Z" fill="#7a6fe0"/><circle cx="26" cy="24" r="11" fill="#fff"/></svg>
<svg class="abs pin" style="left:925px;top:2772px" width="52" height="68" viewBox="0 0 52 68"><path d="M26 66C26 66 50 40 50 24A24 24 0 0 0 2 24C2 40 26 66 26 66Z" fill="#f5a63a"/><circle cx="26" cy="24" r="11" fill="#fff"/></svg>

<!-- BLOG -->
<div class="abs center eyebrow" style="top:3045px">RESOURCES</div>
<h2 class="abs center heading sec-title" style="top:3066px">News And Blog</h2>
<div class="abs nav-arrow" style="left:81px"><svg width="22" height="16" viewBox="0 0 22 16" fill="none" stroke="#fff" stroke-width="2"><path d="M21 8H2M8 2L2 8l6 6"/></svg></div>
<div class="abs nav-arrow" style="left:1088px"><svg width="22" height="16" viewBox="0 0 22 16" fill="none" stroke="#fff" stroke-width="2"><path d="M1 8h19M14 2l6 6-6 6"/></svg></div>

<article class="abs blog-card" style="left:165px;background:linear-gradient(180deg,#cfc8bf,#8b7a6e 45%,#3f3a38)" role="img" aria-label="Photo of a man reading at a desk">
  <div style="margin-top:190px"><span class="date">17 Apr. 2023</span></div>
  <h3>LOREM IPSUM SIT AMET<br>CONSECTETUR</h3>
  <div class="more">READ MORE</div>
</article>
<article class="abs blog-card" style="left:467px;background:linear-gradient(180deg,#e8a55a,#bfb076 45%,#7cc36f)">
  <div style="margin-top:40px"><span class="date">17 Apr. 2023</span></div>
  <h3>LOREM IPSUM SIT AMET<br>CONSECTETUR</h3>
  <p>Lorem ipsum dolor sit amet consectetur. In nulla viverra gravida dictumst volutpat tellus nisl eu. Morbi mi sed dis quis volutpat netus. Phasellus gravida purus integer magn...</p>
  <div class="more">READ MORE</div>
</article>
<article class="abs blog-card" style="left:770px;background:linear-gradient(180deg,#c8c2b8,#8a7a6a 45%,#3d3633)" role="img" aria-label="Photo of hands holding coffee over a travel map">
  <div style="margin-top:190px"><span class="date">17 Apr. 2023</span></div>
  <h3>LOREM IPSUM SIT AMET<br>CONSECTETUR</h3>
  <div class="more">READ MORE</div>
</article>

<!-- FOOTER -->
<div class="abs footer-photo" role="img" aria-label="Blurred photo of a white seaside town terrace"></div>
<svg class="abs footer" viewBox="0 0 1200 466" width="1200" height="466">
  <path d="M0 80 C300 40 600 10 900 20 C1050 25 1150 60 1200 100 L1200 466 L0 466Z" fill="#0e5a6c"/>
  <path d="M100 100 C400 110 700 70 950 40 C1050 30 1150 60 1200 120 L1200 140 C1150 90 1050 60 950 70 C700 100 400 120 100 100Z" fill="#fff"/>
  <path d="M0 130 C300 140 700 110 1000 80 C1100 75 1170 110 1200 160 L1200 466 L0 466Z" fill="#0e5a6c"/>
</svg>
<div class="abs f-brand"><span class="brand-mark" style="width:36px;height:36px"></span><span class="brand-name" style="font-size:20px">HERONFIELD<br>GLOBAL</span></div>
<p class="abs f-about">Our tailored travel services elevate your business travel experience. Let us take you to greater heights, whether you're new or a seasoned traveler. Visit our landing page for details.</p>
<div class="abs f-follow">Follow us on: <i></i><i></i><i></i></div>
<div class="abs f-col" style="left:558px"><h4>SERVICES</h4><ul><li>International Hotel Reservation</li><li>Worldwide Flight Tickets Booking</li><li>Worldwide Travel Arrangement</li><li>Visa services</li><li>Duty Free Goods</li><li>VIP Airport Concierge</li><li>International Business Resources</li></ul></div>
<div class="abs f-col" style="left:782px"><h4>COMPANY</h4><ul><li>About Us</li><li>News and Blog</li><li>Services</li><li>Contact Us</li></ul></div>
<div class="abs f-col f-contact" style="left:924px"><h4>CONTACT</h4><ul>
  <li><svg width="12" height="15" viewBox="0 0 12 15" fill="none" stroke="#fff" stroke-width="1.2"><path d="M6 14s5-5 5-8.5A5 5 0 0 0 1 5.5C1 9 6 14 6 14z"/><circle cx="6" cy="5.5" r="1.8"/></svg><span>2719 Larkspur Ave. Fairhaven,<br>Oregon 97204</span></li>
  <li><svg width="13" height="11" viewBox="0 0 14 12" fill="none" stroke="#fff" stroke-width="1.2"><rect x="1" y="1.5" width="12" height="9"/><path d="M1 2l6 5 6-5"/></svg><span style="font-size:11px">hello@heronfield.com</span></li>
  <li><svg width="12" height="12" viewBox="0 0 12 12" fill="none" stroke="#fff" stroke-width="1.2"><path d="M2 1h2.5l1 3-1.5 1a7 7 0 0 0 3 3l1-1.5 3 1V10a1 1 0 0 1-1 1A9 9 0 0 1 1 2a1 1 0 0 1 1-1z"/></svg><span style="font-size:11px">(503) 555-0187</span></li>
</ul></div>
<div class="abs f-rule"></div>
<div class="abs copy">Copyright HeronfieldGlobal &nbsp;| All rights reserved</div>

</body>
</html>
```